Night Dresses business cards business requirers

We are a new company initiating Mexico operations. Our core business is Night woman dress (both formal and party dress) for rent. Gownhaven is the name of the company. ITS Gownhaven form by two word. The dress word and topia (Utopic) so the place Gownhaven Means That You cant get the ideal, perfect and unique dress for your event. So we would like a modern, very creative, and attractive business card.

Industry/Entity Type

Womens Clothing

Contact Information for Business Card

Rounded Borders, two faces

Requirements
Must have
• Rounded borders, logo and slogan, modern, glam, attractive design
Should not have
• modern design classic or not

```html
<!DOCTYPE html>
<html lang="en">
<head>
<meta charset="utf-8">
<title>Gownhaven Business Cards</title>
<link rel="stylesheet" href="https://fonts.googleapis.com/css2?family=Carlito:ital,wght@0,400;0,700;1,400&display=swap">
<style>
  :root {
    --backdrop: #1f1f21;
    --card: #ffffff;
    --plum: #a0578c;
    --lilac: #c99cc3;
    --pale-lilac: #ecd7ea;
    --orchid: #b25c9c;
    --ink: #4b4b4d;
    --ink-soft: #5a5a5c;
    --font-text: "Carlito", "Calibri", Arial, sans-serif;
  }
  * { box-sizing: border-box; margin: 0; padding: 0; }
  html, body { width: 1200px; height: 999px; overflow: hidden; }
  body { background: var(--backdrop); font-family: var(--font-text); position: relative; }

  .card {
    position: absolute;
    width: 793px; height: 452px;
    background: var(--card);
    border-radius: 40px;
    overflow: hidden;
  }
  .card--front { left: 85px; top: 48px; }
  .card--back  { left: 280px; top: 518px; }

  .card__wave { position: absolute; left: 0; top: 0; width: 793px; height: 452px; }

  .brand { position: absolute; display: flex; align-items: center; }
  .brand__circle { border: 2.5px solid var(--orchid); border-radius: 50%; flex: none; }
  .brand__name { color: var(--ink); font-weight: 400; line-height: 1; }

  .card--front .brand { left: 35px; top: 230px; }
  .card--front .brand__circle { width: 74px; height: 74px; margin-right: 20px; }
  .card--front .brand__name { font-size: 28px; letter-spacing: 4.5px; }

  .card--back .brand { left: 122px; top: 222px; }
  .card--back .brand__circle { width: 110px; height: 110px; margin-right: 36px; }
  .card--back .brand__name { font-size: 46px; letter-spacing: 8px; }

  .person { position: absolute; left: 37px; top: 338px; }
  .person__name { font-size: 36px; font-style: italic; color: var(--orchid); line-height: 1.1; }
  .person__role { font-size: 19px; color: var(--ink-soft); margin-top: 2px; }

  .divider { position: absolute; left: 414px; top: 262px; width: 8px; height: 176px; }

  .contact { position: absolute; left: 506px; top: 262px; color: var(--ink-soft); font-size: 19px; }
  .contact__address { line-height: 25px; }
  .contact__list { list-style: none; margin-top: 22px; }
  .contact__item { display: flex; align-items: center; height: 29.5px; }
  .contact__icon { width: 17px; height: 17px; margin-right: 20px; flex: none; }

  .tagline {
    position: absolute; left: 0; right: 0; top: 367px;
    text-align: center; font-size: 19px; color: var(--ink);
  }
</style>
</head>
<body>

<section class="card card--front">
  <svg class="card__wave" viewBox="0 0 793 452" aria-hidden="true">
    <defs>
      <linearGradient id="streakFront" x1="0" y1="0" x2="1" y2="0">
        <stop offset="0" stop-color="#b784bd"/>
        <stop offset="0.3" stop-color="#ead6ea"/>
        <stop offset="0.5" stop-color="#ffffff"/>
        <stop offset="0.8" stop-color="#efe1ef"/>
        <stop offset="1" stop-color="#f6d7c2"/>
      </linearGradient>
    </defs>
    <path role="img" aria-label="Soft pink and lilac streaks" fill="url(#streakFront)"
          d="M0,0 H793 V95 C720,140 640,170 545,150 C470,132 420,80 330,60 C200,35 80,110 0,190 Z"/>
    <path d="M0,210 C80,120 200,60 330,72 C420,82 470,130 545,152 C640,180 720,150 793,110"
          fill="none" stroke="#ffffff" stroke-width="30"/>
    <path d="M0,222 C80,132 200,72 330,84 C420,94 470,142 545,164 C640,192 720,162 793,122"
          fill="none" stroke="var(--pale-lilac)" stroke-width="26"/>
    <path d="M0,200 C80,110 200,50 330,62 C420,72 470,120 545,142 C640,170 720,140 793,100"
          fill="none" stroke="var(--lilac)" stroke-width="20"/>
    <path d="M0,210 C80,120 200,60 330,72 C420,82 470,130 545,152 C640,180 720,150 793,110"
          fill="none" stroke="var(--plum)" stroke-width="8"/>
  </svg>

  <div class="brand">
    <span class="brand__circle"></span>
    <span class="brand__name">GOWNHAVEN</span>
  </div>

  <div class="person">
    <p class="person__name">Name Title</p>
    <p class="person__role">designation</p>
  </div>

  <svg class="divider" viewBox="0 0 8 176" aria-hidden="true">
    <path d="M4,0 C5.5,60 5.5,116 4,176 C2.5,116 2.5,60 4,0 Z" fill="var(--orchid)"/>
  </svg>

  <div class="contact">
    <p class="contact__address">suit # 00, Lorem ipsum<br>Lorem Lorem ipsum</p>
    <ul class="contact__list">
      <li class="contact__item">
        <svg class="contact__icon" viewBox="0 0 17 17" aria-hidden="true">
          <rect width="17" height="17" rx="3" fill="var(--orchid)"/>
          <path d="M6,3.5 C4,4.5 4,7 5.5,9.5 C7,12 9.5,13.8 11.5,13.5 L12.5,11.5 L10.5,10 L9.5,11 C8.3,10.5 7,9 6.5,7.5 L7.5,6.5 L6.5,3.5 Z" fill="#fff"/>
        </svg>
        <span>000-000-0000</span>
      </li>
      <li class="contact__item">
        <svg class="contact__icon" viewBox="0 0 17 17" aria-hidden="true">
          <rect x="4" y="1" width="9" height="5" fill="var(--orchid)"/>
          <rect x="1" y="7" width="15" height="6" rx="1" fill="var(--orchid)"/>
          <rect x="4" y="14" width="9" height="3" fill="var(--orchid)"/>
        </svg>
        <span>000-000-0000</span>
      </li>
      <li class="contact__item">
        <svg class="contact__icon" viewBox="0 0 17 17" aria-hidden="true">
          <path d="M1,7 L8.5,2 L16,7 V15 H1 Z" fill="var(--orchid)"/>
          <path d="M1,7 L8.5,12 L16,7" fill="none" stroke="#fff" stroke-width="1.4"/>
        </svg>
        <span>abcd@mailbox.com</span>
      </li>
    </ul>
  </div>
</section>

<section class="card card--back">
  <svg class="card__wave" viewBox="0 0 793 452" aria-hidden="true">
    <defs>
      <linearGradient id="streakBack" x1="0" y1="0" x2="1" y2="0">
        <stop offset="0" stop-color="#b07fbd"/>
        <stop offset="0.28" stop-color="#e7d2e8"/>
        <stop offset="0.45" stop-color="#ffffff"/>
        <stop offset="0.75" stop-color="#eddff0"/>
        <stop offset="1" stop-color="#f2b6cf"/>
      </linearGradient>
    </defs>
    <path role="img" aria-label="Soft pink and lilac streaks" fill="url(#streakBack)"
          d="M0,0 H793 V130 C720,170 640,205 545,190 C470,176 410,110 330,95 C200,72 80,140 0,215 Z"/>
    <path d="M0,238 C80,150 200,95 330,105 C420,112 470,160 545,182 C640,210 720,185 793,145"
          fill="none" stroke="#ffffff" stroke-width="30"/>
    <path d="M0,250 C80,162 200,107 330,117 C420,124 470,172 545,194 C640,222 720,197 793,157"
          fill="none" stroke="var(--pale-lilac)" stroke-width="26"/>
    <path d="M0,228 C80,140 200,85 330,95 C420,102 470,150 545,172 C640,200 720,175 793,135"
          fill="none" stroke="var(--lilac)" stroke-width="20"/>
    <path d="M0,238 C80,150 200,95 330,105 C420,112 470,160 545,182 C640,210 720,185 793,145"
          fill="none" stroke="var(--plum)" stroke-width="8"/>
  </svg>

  <div class="brand">
    <span class="brand__circle"></span>
    <span class="brand__name">GOWNHAVEN</span>
  </div>

  <p class="tagline">modern, glam , attractive design</p>
</section>

</body>
</html>
```